shop signs for newquay all year round

We require a shop front signage
2 x 2.5m Long by 1.5m High (sides)
1 x 8m long by 0.7m High (front)

The front sign must read - Penny Wise Bargain Store with the last 1.5m showing the the Xmas Shop open all year (see image 1)

The side signs must have a big bold Arrow pointing Left and one Pointing Right with the words Clearance Sale Now On (see image 2)

Colors

Designer to choose colors to be used in the design.

Requirements
Must have
• signs must be bold and clear to get shoppers into the store, it must be bright and stand out
Nice to have
• good graphics and artwork
Should not have
• plain text

```html
<!DOCTYPE html>
<html lang="en">
<head>
<meta charset="utf-8">
<title>Penny Wise Bargain Store – Shop Signs</title>
<link href="https://fonts.googleapis.com/css2?family=Archivo+Black&family=Alfa+Slab+One&family=Anton&family=Black+Ops+One&display=swap" rel="stylesheet">
<style>
  :root {
    --red-deep: #7a0c16;
    --red-glow: #d9355c;
    --brown: #3e1009;
    --white: #ffffff;
    --green-text: #7cc242;
    --green-arrow: #3aaa3c;
    --blue-arrow: #2f6fc4;
    --gold-light: #f6dd8e;
    --gold-dark: #c8912e;
    --orange: #f4b51b;
    --yellow: #f7e62b;
    --yellow-light: #fbf170;
    --sale-red: #d71f45;
    --bag-blue: #2b3a93;
  }
  html, body {
    margin: 0;
    width: 1200px;
    height: 1200px;
    overflow: hidden;
    background: var(--white);
  }
  .canvas { position: relative; width: 1200px; height: 1200px; }
  .sign { position: absolute; display: block; }
  .sign--front { left: 78px; top: 110px; width: 1038px; height: 415px; }
  .sign--side { left: 78px; top: 621px; width: 1040px; height: 123px; }
  .store-name { font-family: "Black Ops One", sans-serif; fill: var(--white); }
  .store-tag { font-family: "Archivo Black", sans-serif; fill: var(--green-text); }
  .xmas-the { font-family: "Alfa Slab One", serif; fill: var(--white); }
  .xmas-word { font-family: "Anton", sans-serif; fill: url(#goldFill); }
  .xmas-toy { font-family: "Alfa Slab One", serif; fill: var(--orange); }
  .sale-text { font-family: "Archivo Black", sans-serif; fill: var(--sale-red); }
  .bag-label { font-family: "Archivo Black", sans-serif; fill: var(--white); }
</style>
</head>
<body>
<main class="canvas">

  <svg class="sign sign--front" viewBox="0 0 1038 415" aria-label="Penny Wise Bargain Store, The Xmas and Toy Shop">
    <defs>
      <radialGradient id="frontGlow" cx="0.55" cy="0.2" r="0.75">
        <stop offset="0" stop-color="var(--red-glow)"/>
        <stop offset="1" stop-color="var(--red-deep)"/>
      </radialGradient>
      <linearGradient id="groundFill" x1="0" y1="0" x2="0" y2="1">
        <stop offset="0" stop-color="#6b1a10"/>
        <stop offset="1" stop-color="var(--brown)"/>
      </linearGradient>
      <linearGradient id="goldFill" x1="0" y1="0" x2="1" y2="1">
        <stop offset="0" stop-color="var(--gold-light)"/>
        <stop offset="0.5" stop-color="var(--gold-dark)"/>
        <stop offset="1" stop-color="var(--gold-light)"/>
      </linearGradient>
      <linearGradient id="treatsFill" x1="0" y1="0" x2="1" y2="1">
        <stop offset="0" stop-color="#c97a3e"/>
        <stop offset="1" stop-color="#8a3f1c"/>
      </linearGradient>
      <radialGradient id="pineFill">
        <stop offset="0" stop-color="#3d8a2a"/>
        <stop offset="1" stop-color="#16421a" stop-opacity="0"/>
      </radialGradient>
    </defs>

    <rect class="front-bg" width="1038" height="415" fill="url(#frontGlow)"/>
    <path class="front-ground" d="M0 360 C200 320 420 340 600 380 C760 410 900 350 1038 330 L1038 415 L0 415 Z" fill="url(#groundFill)"/>

    <ellipse class="pine-branch" role="img" aria-label="Pine branches" cx="1010" cy="120" rx="70" ry="170" fill="url(#pineFill)"/>
    <ellipse class="pine-branch" role="img" aria-label="Pine branches" cx="30" cy="380" rx="80" ry="70" fill="url(#pineFill)"/>
    <ellipse class="treats-art" role="img" aria-label="Christmas gingerbread cookies and candy canes" cx="880" cy="300" rx="175" ry="150" fill="url(#treatsFill)" opacity="0.85"/>
    <ellipse class="candy-art" role="img" aria-label="Wrapped Christmas sweets" cx="640" cy="355" rx="80" ry="40" fill="#b8312a" opacity="0.8"/>
    <ellipse class="candy-art" role="img" aria-label="Wrapped Christmas sweet" cx="75" cy="235" rx="55" ry="22" fill="#b8312a" opacity="0.8" transform="rotate(-35 75 235)"/>

    <text class="store-name" x="56" y="92" font-size="56" textLength="250" lengthAdjust="spacingAndGlyphs">PENNY</text>
    <text class="store-name" x="56" y="148" font-size="56" textLength="250" lengthAdjust="spacingAndGlyphs">WISE</text>
    <text class="store-tag" x="320" y="106" font-size="60">BARGAIN</text>
    <text class="store-tag" x="320" y="162" font-size="60">STORE</text>

    <g class="pointer-arrow" transform="translate(632 172) rotate(-135) translate(-58 0)">
      <polygon points="0,-22 62,-22 62,-52 116,0 62,52 62,22 0,22" fill="var(--blue-arrow)" stroke="var(--white)" stroke-width="5" stroke-linejoin="round"/>
      <polygon points="8,-14 70,-14 70,-36 104,0 70,36 70,14 8,14" fill="none" stroke="var(--white)" stroke-width="1.5" stroke-dasharray="4 3"/>
    </g>

    <text class="xmas-the" x="82" y="280" font-size="40" textLength="80" lengthAdjust="spacingAndGlyphs">THE</text>
    <text class="xmas-word" x="168" y="348" font-size="190" textLength="80" lengthAdjust="spacingAndGlyphs">X</text>
    <text class="xmas-word" x="262" y="337" font-size="116" textLength="226" lengthAdjust="spacingAndGlyphs">MAS</text>
    <text class="xmas-toy" x="495" y="274" font-size="38" textLength="211" lengthAdjust="spacingAndGlyphs">&amp; TOY SHOP</text>
  </svg>

  <svg class="sign sign--side" viewBox="0 0 1040 123" aria-label="Clearance sale now on">
    <defs>
      <radialGradient id="sideGlow" cx="0.5" cy="0.5" r="0.7">
        <stop offset="0" stop-color="var(--yellow-light)"/>
        <stop offset="1" stop-color="var(--yellow)"/>
      </radialGradient>
    </defs>
    <rect class="side-bg" width="1040" height="123" fill="url(#sideGlow)"/>

    <g class="direction-arrow direction-arrow--left">
      <polygon points="12,63 90,17 90,38 166,38 166,88 90,88 90,109" fill="var(--green-arrow)" stroke="var(--white)" stroke-width="4" stroke-linejoin="round"/>
      <polygon points="24,63 84,28 84,46 158,46 158,80 84,80 84,98" fill="none" stroke="var(--white)" stroke-width="1.5" stroke-dasharray="4 3"/>
    </g>
    <g class="direction-arrow direction-arrow--right" transform="translate(1040 0) scale(-1 1)">
      <polygon points="12,63 90,17 90,38 166,38 166,88 90,88 90,109" fill="var(--green-arrow)" stroke="var(--white)" stroke-width="4" stroke-linejoin="round"/>
      <polygon points="24,63 84,28 84,46 158,46 158,80 84,80 84,98" fill="none" stroke="var(--white)" stroke-width="1.5" stroke-dasharray="4 3"/>
    </g>

    <text class="sale-text" x="192" y="84" font-size="46" textLength="286" lengthAdjust="spacingAndGlyphs">CLEARANCE</text>
    <text class="sale-text" x="650" y="84" font-size="46" textLength="204" lengthAdjust="spacingAndGlyphs">NOW ON</text>

    <g class="sale-bags">
      <polygon points="518,22 584,22 590,116 494,104" fill="var(--bag-blue)"/>
      <path d="M540 22 C540 2 560 2 560 22" fill="none" stroke="#222" stroke-width="2"/>
      <polygon points="534,22 622,14 640,100 560,112" fill="var(--sale-red)"/>
      <path d="M565 20 C562 -2 596 -4 598 17" fill="none" stroke="#222" stroke-width="2"/>
      <text class="bag-label" x="530" y="84" font-size="34" textLength="100" lengthAdjust="spacingAndGlyphs">SALE</text>
    </g>
  </svg>

</main>
</body>
</html>
```